Roof Plumbing Company needs simple, modern business card using the attached logo and below details:

Dean Halloway
Summit Gutters Pty Ltd
ABN: 58 214 937 062
Phone: 0417 286 531
Email: summitgutters@mailbrook.com
Website: summitgutters.com.au

For all of your metal roof plumbing requirements contact Summit Gutters for an obligation free quote - no job too big or to small!

Industry/Entity Type

Business

Contact Information for Business Card

Dean Halloway
Summit Gutters Pty Ltd
ABN 58 214 937 062
0417 286 531
summitgutters@mailbrook.com
summitgutters.com.au

Requirements
Must have
• Bright eye catching design, professional look

```html
<!DOCTYPE html>
<html lang="en">
<head>
<meta charset="utf-8">
<title>Summit Gutters Pty Ltd – Business Card</title>
<link rel="stylesheet" href="https://fonts.googleapis.com/css2?family=Arimo:wght@400;700&family=Open+Sans:wght@400;600&display=swap">
<style>
  :root {
    --brand-red: #d32628;
    --card-white: #ffffff;
    --ink-dark: #2b2b2b;
    --footer-dark: #2f2b2b;
    --text-light: #ffffff;
  }
  * { margin: 0; padding: 0; box-sizing: border-box; }
  html, body {
    width: 1200px; height: 686px; overflow: hidden;
    background: var(--card-white);
  }
  .card {
    position: relative; width: 1200px; height: 686px;
    background: var(--card-white);
    font-family: "Open Sans", Arial, sans-serif;
  }
  .brand-name {
    position: absolute; left: 74px; top: 96px;
    display: flex; align-items: center; gap: 14px;
    color: var(--brand-red);
    font-family: "Open Sans", Arial, sans-serif;
    font-weight: 600; font-size: 34px; line-height: 1.1;
  }
  .brand-mark {
    width: 22px; height: 22px; background: var(--brand-red);
  }
  .tagline {
    position: absolute; right: 78px; top: 114px;
    font-family: "Arimo", Arial, sans-serif;
    font-size: 42px; line-height: 1; color: var(--ink-dark);
    letter-spacing: -0.3px;
  }
  .tagline strong { font-weight: 700; }
  .tagline .light { font-weight: 400; }
  .contact-band {
    position: absolute; left: 0; top: 270px; width: 1200px; height: 320px;
    background: var(--brand-red); color: var(--text-light);
    text-align: center;
  }
  .icon-house { position: absolute; left: 573px; top: 30px; }
  .company-details {
    position: absolute; left: 0; right: 0; top: 90px;
    font-weight: 600; font-size: 27px; line-height: 36px;
  }
  .band-divider {
    position: absolute; left: 349px; top: 181px; width: 502px; height: 2px;
    background: linear-gradient(90deg, rgba(255,255,255,0), rgba(255,255,255,0.55), rgba(255,255,255,0));
  }
  .icon-phone { position: absolute; left: 573px; top: 202px; }
  .phone-number {
    position: absolute; left: 0; right: 0; top: 255px;
    font-weight: 600; font-size: 27px;
  }
  .footer {
    position: absolute; left: 0; top: 599px; width: 1200px; height: 87px;
    background: var(--footer-dark); color: var(--text-light);
    font-size: 23px;
  }
  .footer-item {
    position: absolute; top: 0; height: 87px;
    display: flex; align-items: center; gap: 16px;
  }
  .footer-web { left: 74px; }
  .footer-email { right: 78px; }
</style>
</head>
<body>
<main class="card">
  <div class="brand-name"><span class="brand-mark"></span><span>Summit Gutters</span></div>

  <p class="tagline"><strong>NO JOB TOO BIG OR TO</strong> <span class="light">SMALL!</span></p>

  <section class="contact-band">
    <svg class="icon-house" width="54" height="46" viewBox="0 0 54 46" aria-hidden="true">
      <path d="M27 2 L2 24 L7 24 L27 7 L47 24 L52 24 Z" fill="#fff"/>
      <path d="M10 24 L27 10 L44 24 L44 44 L32 44 L32 31 L22 31 L22 44 L10 44 Z" fill="#fff"/>
    </svg>
    <div class="company-details">
      <p>Dean Halloway Summit Gutters Pty Ltd</p>
      <p>ABN 58 214 937 062</p>
    </div>
    <div class="band-divider"></div>
    <svg class="icon-phone" width="54" height="42" viewBox="0 0 54 42" aria-hidden="true">
      <path d="M3 14 C3 4 51 4 51 14 L51 18 L40 18 L40 12 C34 9 20 9 14 12 L14 18 L3 18 Z" fill="#fff"/>
      <path d="M16 16 L38 16 L46 30 L46 40 L8 40 L8 30 Z" fill="#fff"/>
      <g fill="#d32628">
        <rect x="20" y="22" width="4" height="3"/><rect x="25" y="22" width="4" height="3"/><rect x="30" y="22" width="4" height="3"/>
        <rect x="20" y="27" width="4" height="3"/><rect x="25" y="27" width="4" height="3"/><rect x="30" y="27" width="4" height="3"/>
        <rect x="20" y="32" width="4" height="3"/><rect x="25" y="32" width="4" height="3"/><rect x="30" y="32" width="4" height="3"/>
      </g>
    </svg>
    <p class="phone-number">0417 286 531</p>
  </section>

  <footer class="footer">
    <div class="footer-item footer-web">
      <svg width="30" height="30" viewBox="0 0 30 30" aria-hidden="true" fill="none" stroke="#fff" stroke-width="2">
        <circle cx="15" cy="15" r="13"/>
        <ellipse cx="15" cy="15" rx="6" ry="13"/>
        <line x1="2" y1="15" x2="28" y2="15"/>
        <path d="M4.5 8 H25.5 M4.5 22 H25.5"/>
      </svg>
      <span>summitgutters.com.au</span>
    </div>
    <div class="footer-item footer-email">
      <svg width="30" height="22" viewBox="0 0 30 22" aria-hidden="true" fill="none" stroke="#fff" stroke-width="2">
        <rect x="1" y="1" width="28" height="20"/>
        <path d="M1 1 L15 13 L29 1 M1 21 L11 10 M29 21 L19 10"/>
      </svg>
      <span>summitgutters@mailbrook.com</span>
    </div>
  </footer>
</main>
</body>
</html>
```